Simple and Clean business card design

We would like the design to be simple clean and to incorporate our colors.

We are open to your design and talent, we have the dots in our logo as we think of it as data points and we connect data points for people.

We are open to see the great creative and clean design you bring to the table

Contact Information for Business Card

please include: name, position, email, phone and website

Font styles to use
Sans Serif

Requirements
Must have
• my colors incorporated, simplicity
Nice to have
• lots of white space, simplicity
Should not have
• complexicity/ complex art

```html
<!DOCTYPE html>
<html lang="en">
<head>
<meta charset="utf-8">
<title>Vantle business card</title>
<link href="https://fonts.googleapis.com/css2?family=Montserrat:wght@400;500;600;700&display=swap" rel="stylesheet">
<style>
  :root {
    --stage: #e3e4e6;
    --card: #17191d;
    --edge: #3d7fe6;
    --ink: #f2f3f5;
    --muted: #c9ccd1;
    --accent: #4285f4;
  }
  * { box-sizing: border-box; margin: 0; padding: 0; }
  html, body { width: 1200px; height: 800px; overflow: hidden; }
  body {
    background: var(--stage);
    font-family: "Montserrat", sans-serif;
    position: relative;
  }
  .card {
    position: absolute;
    top: 250px;
    width: 520px;
    height: 300px;
    background: var(--card);
    border-radius: 22px;
    border-bottom: 4px solid var(--edge);
    overflow: hidden;
  }
  .card--front { left: 60px; }
  .card--back { left: 620px; }

  .brand {
    display: flex;
    align-items: center;
    gap: 10px;
    color: var(--ink);
    font-weight: 700;
    letter-spacing: 0.5px;
  }
  .brand__dot {
    border-radius: 50%;
    background: var(--accent);
    flex: none;
  }

  .card--front .brand { position: absolute; left: 48px; top: 96px; font-size: 34px; }
  .card--front .brand__dot { width: 14px; height: 14px; }

  .identity { position: absolute; left: 48px; top: 158px; }
  .identity__name { color: var(--ink); font-size: 20px; font-weight: 600; }
  .identity__role { color: var(--accent); font-size: 14px; font-weight: 500; margin-top: 2px; }

  .contact { position: absolute; left: 48px; top: 218px; list-style: none; }
  .contact__item {
    display: flex; align-items: center; gap: 9px;
    color: var(--muted); font-size: 13px; line-height: 20px;
  }
  .contact__icon { width: 12px; height: 12px; fill: var(--accent); flex: none; }

  .card--back { display: flex; align-items: center; justify-content: center; }
  .card--back .brand { font-size: 64px; gap: 16px; }
  .card--back .brand__dot { width: 26px; height: 26px; }
</style>
</head>
<body>
  <article class="card card--front">
    <div class="brand"><span class="brand__dot"></span>Vantle</div>
    <div class="identity">
      <p class="identity__name">Daniel Reyes</p>
      <p class="identity__role">President</p>
    </div>
    <ul class="contact">
      <li class="contact__item">
        <svg class="contact__icon" viewBox="0 0 24 24" aria-hidden="true"><path d="M6.6 10.8a15.1 15.1 0 0 0 6.6 6.6l2.2-2.2a1 1 0 0 1 1-.25 11.4 11.4 0 0 0 3.6.57 1 1 0 0 1 1 1V20a1 1 0 0 1-1 1A17 17 0 0 1 3 4a1 1 0 0 1 1-1h3.5a1 1 0 0 1 1 1c0 1.25.2 2.45.57 3.57a1 1 0 0 1-.25 1z"/></svg>
        555-014-2287
      </li>
      <li class="contact__item">
        <svg class="contact__icon" viewBox="0 0 24 24" aria-hidden="true"><path d="M2 5h20v14H2zm2 2v.5l8 5 8-5V7l-8 5z"/></svg>
        info@vantle.com
      </li>
      <li class="contact__item">
        <svg class="contact__icon" viewBox="0 0 24 24" aria-hidden="true"><path d="M12 2a10 10 0 1 0 0 20 10 10 0 0 0 0-20zm6.9 9h-3a15 15 0 0 0-1.3-5.6A8 8 0 0 1 18.9 11zM12 4.1c.9 1.2 1.8 3.6 1.9 6.9h-3.8c.1-3.3 1-5.7 1.9-6.9zM9.4 5.4A15 15 0 0 0 8.1 11h-3a8 8 0 0 1 4.3-5.6zM5.1 13h3a15 15 0 0 0 1.3 5.6A8 8 0 0 1 5.1 13zm6.9 6.9c-.9-1.2-1.8-3.6-1.9-6.9h3.8c-.1 3.3-1 5.7-1.9 6.9zm2.6-1.3a15 15 0 0 0 1.3-5.6h3a8 8 0 0 1-4.3 5.6z"/></svg>
        vantle.com
      </li>
    </ul>
  </article>

  <article class="card card--back">
    <div class="brand"><span class="brand__dot"></span>Vantle</div>
  </article>
</body>
</html>
```